Business card for a new innovative and professional lawn care business

We need a business card design for a new lawn care business in Halifax NS Canada. We offer lawn services in Halifax & Bedford. Our services offered include lawn care, garden services, and property maintenance. We take pride in our work and are experienced at what we do. I would like to see a design that is double sided. On the backside I would like the something simple (maybe my logo preferably on blackround (linked below) with website link, Facebook page or something). The front I want to include contact info:
Darren Maple
phone 902-555-0148
email - darrensyardworks.ca
facebook - Facebook.com/darrensyardworks
Instagram maybe ? - instagram.com/darrenyardworks
Serving Halifax and Bedford for 5 years?
I don't want it to have too much information as I will be passing them out in aim to visit website, or call !
We do want it to include lawn care, garden services and property maintenance.
Basic, catchy, and modern looking !
Logo attached below !

Target Market(s)

Passing business cards to everyone I meet or interact with.

Industry/Entity Type

Lawn Care

Contact Information for Business Card

Double sided with some basic information, with catchy colours and easy to look at.

Font styles to use
Sans Serif

Requirements
Must have
• Must be double sided and have :
• Name, Phone, Email, FB, Website, and 3 main services offered - lawn care, property maintenance, garden services
Nice to have
• Would be nice to have instagram link if it goes well on there
Should not have
• Don't want too much writing or images that are distracting

```html
<!DOCTYPE html>
<html lang="en">
<head>
<meta charset="utf-8">
<title>Darren's Yard Works – Business Cards</title>
<link rel="stylesheet" href="https://fonts.googleapis.com/css2?family=Open+Sans:wght@600;800&display=swap">
<style>
  :root {
    --page: #e6e6e6;
    --card: #ffffff;
    --frame: #6ab04c;
    --ink: #2b2b2b;
    --brand: #7cc242;
    --deep: #0b4d12;
    --mid: #1f8a25;
    --lime: #b9e24a;
    --night: #000000;
  }
  * { box-sizing: border-box; margin: 0; padding: 0; }
  html, body { width: 1200px; height: 741px; overflow: hidden; }
  body {
    position: relative;
    background: var(--page);
    font-family: "Open Sans", sans-serif;
    font-weight: 600;
    color: var(--ink);
  }
  .card { position: absolute; overflow: hidden; background: var(--card); }
  .card--front, .card--about { border: 6px solid var(--frame); }

  .wave { position: absolute; left: 0; bottom: 0; width: 100%; height: 84px; }

  .card--front { left: 496px; top: 34px; width: 510px; height: 292px; }
  .contact {
    position: absolute; right: 4px; top: 2px; width: 300px;
    text-align: center; font-size: 20px; line-height: 29px;
  }
  .brand-name {
    position: absolute; left: 22px; top: 116px;
    font-weight: 800; font-size: 31px; letter-spacing: 1px;
    color: var(--brand); white-space: nowrap;
  }
  .social {
    position: absolute; right: 4px; top: 182px;
    text-align: right; font-size: 20px; line-height: 27px;
    white-space: nowrap;
  }

  .card--about { left: 50px; top: 330px; width: 512px; height: 294px; }
  .about-intro {
    position: absolute; left: 6px; top: 2px; width: 496px;
    font-size: 20px; line-height: 29px; white-space: nowrap;
  }
  .about-closing {
    position: absolute; left: 156px; top: 142px; width: 340px;
    font-size: 20px; line-height: 29px; white-space: nowrap;
  }
  .about-closing .last { display: block; padding-left: 72px; }

  .card--back {
    left: 614px; top: 402px; width: 498px; height: 208px;
    padding: 11px;
  }
  .back-panel {
    width: 100%; height: 100%; background: var(--night);
    display: flex; align-items: center; justify-content: center;
  }
  .back-panel .brand-name { position: static; font-size: 36px; }
</style>
</head>
<body>

  <svg width="0" height="0" style="position:absolute" aria-hidden="true">
    <defs>
      <linearGradient id="waveFill" x1="0" y1="0" x2="0" y2="1">
        <stop offset="0" stop-color="#1f8a25"/>
        <stop offset="1" stop-color="#0b4d12"/>
      </linearGradient>
      <g id="grassWave">
        <path d="M0,0 C60,8 120,44 200,56 C300,66 420,62 500,60 L500,84 L0,84 Z" fill="url(#waveFill)"/>
        <path d="M0,36 C100,56 250,76 500,70" fill="none" stroke="#b9e24a" stroke-width="3"/>
        <path d="M0,58 C150,74 350,84 500,74 L500,84 L0,84 Z" fill="#0b4d12"/>
        <path d="M180,81 C320,84 440,80 500,76" fill="none" stroke="#b9e24a" stroke-width="3"/>
      </g>
    </defs>
  </svg>

  <section class="card card--front">
    <svg class="wave" viewBox="0 0 500 84" preserveAspectRatio="none" aria-hidden="true"><use href="#grassWave"/></svg>
    <div class="contact">
      <p>Darren Maple</p>
      <p>phone 902-555-0148</p>
      <p>email - darrensyardworks.ca</p>
    </div>
    <p class="brand-name">DARREN'S YARD WORKS</p>
    <div class="social">
      <p>- instagram.com/darrenyardworks</p>
      <p>Serving Halifax and Bedford for 5 years?</p>
    </div>
  </section>

  <section class="card card--about">
    <svg class="wave" viewBox="0 0 500 84" preserveAspectRatio="none" aria-hidden="true"><use href="#grassWave"/></svg>
    <p class="about-intro">We offer a new lawn care business in Halifax<br>&amp; Bedford. Our services include lawn care, garden<br>services, and property maintenance.<br>We take pride in our work and are experienced at<br>what we do.</p>
    <p class="about-closing">We look forward to maintaining<br>your lawns to your usual pristine<br>conditions &amp; working with new<span class="last">and old customers</span></p>
  </section>

  <section class="card card--back">
    <div class="back-panel">
      <p class="brand-name">DARREN'S YARD WORKS</p>
    </div>
  </section>

</body>
</html>
```